Webdesign für Adressvalidierung
Zielgruppe
Was macht die Firma: Addressvalidierung zur Steigerung der Datenqualität vom Spezialisten.
Zielgruppe: B2B - alle Branchen, die auf Datenqualität setzen.
Aufgabenstellung
Die Herausforderung besteht darin, die umfangreichen Textinhalte optisch ansprechend darzustellen. Hierfür sollten die Beispiel-Designs unbedingt die vorgefertigten Texte für (Meta-Titel, Sub-Headline, Seitenüberschrift etc.) berücksichtigen, damit wir eine genaue Vorstellung über die Website erhalten.

```html
<!DOCTYPE html>
<html lang="en">
<head>
<meta charset="utf-8">
<title>Verifona – Address Validation</title>
<link href="https://fonts.googleapis.com/css2?family=Open+Sans:wght@400;600;700;800&display=swap" rel="stylesheet">
<style>
:root{
  --stage:#dcdcdc;
  --purple:#9a5cf2;
  --blue:#5a6ee8;
  --navy:#0e4b8f;
  --ink:#1f2a3a;
  --text:#6b7280;
  --band:#d7e7f6;
  --card:#f5f6f8;
  --teal:#53d3b6;
  --white:#fff;
}
*{box-sizing:border-box;margin:0;padding:0}
html,body{width:1200px;height:3816px;overflow:hidden}
body{background:linear-gradient(160deg,#f3f3f3 0%,var(--stage) 60%,#cfcfcf 100%);font-family:"Open Sans",sans-serif;color:var(--ink);position:relative}
.abs{position:absolute}
.desk{position:absolute;left:228px;top:560px;width:593px;height:2695px;background:var(--white);overflow:hidden;box-shadow:0 6px 30px rgba(0,0,0,.08)}
.mob{position:absolute;left:1015px;top:0;width:185px;height:3816px;background:var(--white);overflow:hidden}
.hero{background:linear-gradient(100deg,var(--purple),var(--blue))}
.brand{color:var(--white);font-weight:800;letter-spacing:.5px;display:flex;align-items:center;gap:4px;white-space:nowrap}
.brand i{display:block;width:8px;height:8px;border-radius:50%;background:currentColor}
.brand.dark{color:var(--navy)}
.nav{color:#fff;font-size:6px}
.nav span{white-space:nowrap}
.lang{border:1px solid #fff;border-radius:2px;color:#fff;font-size:5px;display:flex;align-items:center;justify-content:center}
.h-title{color:#fff;font-size:13px;font-weight:400;white-space:nowrap}
.h-title b{font-weight:800}
.h-sub{color:#f0eaff;font-size:5.5px;white-space:nowrap}
.btn-w{background:#fff;color:var(--purple);font-size:5.5px;display:flex;align-items:center;justify-content:center}
.btn-o{border:1px solid #fff;color:#fff;font-size:5.5px;display:flex;align-items:center;justify-content:center}
.btn-n{background:var(--navy);color:#fff;font-size:5.5px;display:flex;align-items:center;justify-content:center}
.phone{border:3px solid #111;border-radius:10px;background:#fff}
.addr{background:#fff;border-radius:3px;box-shadow:0 3px 10px rgba(0,0,0,.15);padding:8px 10px;font-size:5px;color:var(--text)}
.addr li{list-style:none;display:flex;justify-content:space-between;align-items:center;height:23px;white-space:nowrap}
.ok,.no{width:8px;height:8px;border-radius:50%;border:1px solid;flex:none}
.ok{border-color:#3ccf8e}.no{border-color:#e95a6b}
.kicker{font-size:5px;color:var(--text);text-align:center}
.sec-title{font-size:13px;font-weight:700;text-align:center}
.feat{padding:18px 17px;font-size:5.5px;line-height:10px;color:var(--text);background:var(--card)}
.feat.on{background:var(--blue);color:#e8ebff}
.feat .ico{width:20px;height:20px;margin-bottom:12px}
.feat h4{font-size:5.5px;font-weight:400;margin-bottom:10px}
.feat h4 b{font-weight:700}
.feat.on h4{color:#fff}
.band{background:var(--band)}
.h3{font-size:9px;font-weight:400;line-height:11px}
.h3 b{font-weight:700}
.body{font-size:5.5px;line-height:10px;color:var(--text)}
.body+.body{margin-top:10px}
.list li{list-style:none;font-size:5.5px;color:var(--text);display:flex;gap:8px;line-height:15.5px}
.list li::before{content:"";flex:none;width:6px;height:6px;border:1px solid #9fb7d8;border-radius:50%;margin-top:4px}
.sol-lead{background:var(--navy);color:#fff;padding:28px 24px}
.sol-lead h3{font-size:13px;font-weight:400;line-height:14px}
.sol-lead h3 b{font-weight:800}
.sol-lead p{font-size:5.5px;line-height:10px;margin-top:14px}
.sol-card{background:var(--card);padding:16px 20px;font-size:5px;line-height:9px;color:var(--text)}
.sol-card h5{color:var(--navy);font-size:7px;font-weight:700;margin-bottom:10px;white-space:nowrap}
.pills{display:flex;gap:8px;margin-top:10px}
.pills span{flex:1;height:11px;font-size:4.5px;display:flex;align-items:center;justify-content:center;border:1px solid var(--navy);color:var(--navy)}
.pills span:first-child{background:var(--navy);color:#fff}
.city{background:linear-gradient(180deg,#e9eef3 0%,#b8a99a 55%,#6d6a72 100%)}
.illus{background:radial-gradient(circle at 50% 60%,#e9f1f7 0 55%,transparent 56%),linear-gradient(135deg,transparent 30%,rgba(83,211,182,.35) 50%,transparent 70%)}
.illus-sq{background:linear-gradient(135deg,#e9f7f2,#bfeee0 60%,#2e3c4e)}
.cta-line{font-size:5.5px;font-weight:700;text-align:center}
.foot h6{font-size:5px;font-weight:700;margin-bottom:10px}
.foot li{list-style:none;font-size:5.5px;color:var(--text);line-height:9px;white-space:nowrap}
.soc{display:flex;gap:8px}
.soc i{width:10px;height:10px;border-radius:50%;background:var(--navy);display:block}
.copy{font-size:5px;color:#9aa3ae;text-align:center}
.m-list div{height:14px;background:var(--navy);color:#fff;font-size:5px;font-weight:700;display:flex;align-items:center;padding:0 8px;justify-content:space-between;white-space:nowrap}
</style>
</head>
<body>

<section class="desk">
  <header class="hero abs" style="left:0;top:0;width:593px;height:329px">
    <div class="brand abs" style="left:33px;top:28px;font-size:10px"><i></i>VERIFONA</div>
    <nav class="nav abs" style="left:0;top:30px;width:593px;height:10px">
      <span class="abs" style="left:234px">Products ⌄</span>
      <span class="abs" style="left:287px">Solutions ⌄</span>
      <span class="abs" style="left:344px">Pricing</span>
      <span class="abs" style="left:395px">Developer</span>
      <span class="abs" style="left:457px">Resources</span>
    </nav>
    <div class="lang abs" style="left:516px;top:26px;width:43px;height:16px">◎ EN ⌄</div>
    <h1 class="h-title abs" style="left:33px;top:124px"><b>ADDRESS VALIDATION:</b> verification &amp; updating | Data quality</h1>
    <p class="h-sub abs" style="left:33px;top:155px">Solutions for digital data verification &amp; address validation. Proven concepts for maximum data quality.</p>
    <div class="btn-w abs" style="left:33px;top:185px;width:107px;height:30px">FIND OUT HOW</div>
    <div class="btn-o abs" style="left:172px;top:185px;width:107px;height:30px">FREE TRIAL</div>
    <svg class="abs" style="left:0;top:180px" width="593" height="150" viewBox="0 0 593 150"><path d="M0 60 C90 110 170 120 260 95 C360 65 430 115 593 150 L593 150 L0 150Z" fill="#fff"/></svg>
    <div class="phone abs" style="left:470px;top:89px;width:87px;height:225px">
      <div class="brand dark abs" style="left:10px;top:95px;font-size:7px"><i></i>VERIFONA</div>
    </div>
    <ul class="addr abs" style="left:327px;top:181px;width:154px;height:130px">
      <li>Lindenweg 4, 10115 Musterstadt<span class="ok"></span></li>
      <li>Ahornstr. 12, 20095 Beispielheim<span class="no"></span></li>
      <li>Birkenallee 8, 30159 Neudorf<span class="ok"></span></li>
      <li>Eschenring 21, 40213 Talhausen<span class="no"></span></li>
      <li>Ulmenpfad 3, 50667 Bergfeld<span class="no"></span></li>
    </ul>
  </header>

  <section class="intro">
    <svg class="abs" style="left:292px;top:366px" width="9" height="12" viewBox="0 0 9 12"><path d="M4.5 0a4.5 4.5 0 0 1 4.5 4.5C9 8 4.5 12 4.5 12S0 8 0 4.5A4.5 4.5 0 0 1 4.5 0z" fill="#0e4b8f"/><circle cx="4.5" cy="4.5" r="1.7" fill="#fff"/></svg>
    <p class="kicker abs" style="left:0;width:593px;top:384px">Your most important contact: tomorrow's customer</p>
    <h2 class="sec-title abs" style="left:0;width:593px;top:396px">Complete solutions for professional address validation</h2>
    <article class="feat on abs" style="left:33px;top:453px;width:151px;height:145px">
      <svg class="ico" viewBox="0 0 20 20"><circle cx="8" cy="8" r="6" fill="none" stroke="#fff"/><path d="M12.5 12.5L19 19" stroke="#fff"/></svg>
      <h4><b>Accurate</b> Global Data</h4>
      Lorem ipsum dolor sit amet, consectetur adipiscing elit. Sed a dignissim neque. Pellentesque pellentesque, sapien at finibus iaculis, eros dolor gravida enim, sit amet interdum turpis eros nec felis.
    </article>
    <article class="feat abs" style="left:220px;top:453px;width:154px;height:145px">
      <svg class="ico" viewBox="0 0 20 20"><path d="M2 18L18 2M6 18L18 6M2 14L14 2" stroke="#5a6ee8" fill="none"/></svg>
      <h4><b>Improved</b> Data Quality</h4>
      Lorem ipsum dolor sit amet, consectetur adipiscing elit. Sed a dignissim neque. Pellentesque pellentesque, sapien at finibus iaculis, eros dolor gravida enim, sit amet interdum turpis eros nec felis.
    </article>
    <article class="feat abs" style="left:408px;top:453px;width:153px;height:145px">
      <svg class="ico" viewBox="0 0 20 20"><path d="M10 1L17 19L10 14L3 19Z" stroke="#5a6ee8" fill="none"/></svg>
      <h4><b>Increased</b> Conversions</h4>
      Lorem ipsum dolor sit amet, consectetur adipiscing elit. Sed a dignissim neque. Pellentesque pellentesque, sapien at finibus iaculis, eros dolor gravida enim, sit amet interdum turpis eros nec felis.
    </article>
  </section>

  <section class="band abs" style="left:0;top:678px;width:593px;height:237px">
    <h3 class="h3 abs" style="left:33px;top:70px;width:340px"><b>More customer contacts, automatically:</b> address validation works</h3>
    <p class="body abs" style="left:33px;top:96px;width:280px">High data quality is the key competitive advantage in today's digital market. It allows companies to target their precious resources, communicate efficiently and rest assured that their customers are actually being reached. Selling just gets better, results can be consistently driven higher. We provide solutions for the address verification you need, supporting you with tried and tested processes for professional address validation. Get in touch. We'd love to talk.</p>
    <div class="illus-sq abs" role="img" aria-label="Isometric illustration of a smartphone showing a city map with location pins" style="left:379px;top:20px;width:204px;height:200px;border-radius:50% 50% 10px 10px;opacity:.85"></div>
  </section>

  <section class="cols">
    <h3 class="h3 abs" style="left:33px;top:984px;width:246px"><b>Address validation as enabler:</b> better contacts just when you need them</h3>
    <div class="abs" style="left:33px;top:1020px;width:246px">
      <p class="body">The benefits of professional address verification are strikingly simple: information on products, services and solutions gets through to the correct recipients, ensuring improved orders and sales. Accurate data means effective direct marketing efforts.</p>
      <p class="body">And it's not just marketing managers this matters to. Senior leaders, too, take a keen interest in maximising return on investment. The bottom line is that professional address verification can mean an identical investment in marketing, customer acquisition and sales simply achieves more.</p>
    </div>
    <h3 class="h3 abs" style="left:340px;top:984px;width:240px"><b>Address verification:</b> key information</h3>
    <ul class="list abs" style="left:340px;top:1018px;width:240px">
      <li>Automatic address verification &amp; integration of missing data</li>
      <li>Verification of e-mail addresses, postal addresses or other fields</li>
      <li>Address correction based on updated reference data</li>
      <li>Powerful software for modern data management</li>
      <li>Proven functionality with a range of benefits</li>
      <li>Personal advice: verified addresses in a snap</li>
    </ul>
  </section>

  <section class="solutions">
    <span class="abs" style="left:538px;top:1158px;font-size:8px;color:#c5cdd8">‹</span>
    <span class="abs" style="left:556px;top:1158px;font-size:8px;color:var(--navy)">›</span>
    <div class="sol-lead abs" style="left:34px;top:1183px;width:152px;height:127px">
      <h3>OUR<br><b>SOLUTIONS</b></h3>
      <p>Discover our outstanding services and get started right away</p>
    </div>
    <div class="sol-card abs" style="left:202px;top:1183px;width:152px;height:127px">
      <h5>⌖ Address Service</h5>
      Lorem ipsum dolor sit amet, consectetur adipiscing elit. Aliquam vitae porta tellus. Proin ultrices dignissim lacus, ac ultrices libero malesuada et.
      <div class="pills"><span>More</span><span>API Keys</span></div>
    </div>
    <div class="sol-card abs" style="left:374px;top:1183px;width:150px;height:127px">
      <h5>⌂ Social Media/eCommerce</h5>
      Lorem ipsum dolor sit amet, consectetur adipiscing elit. Aliquam vitae porta tellus. Proin ultrices dignissim lacus, ac ultrices libero malesuada et.
      <div class="pills"><span>More</span><span>API Keys</span></div>
    </div>
    <div class="sol-card abs" style="left:544px;top:1183px;width:150px;height:127px">
      <h5>◎ GeoLookup</h5>
      Lorem ipsum dolor sit amet, consectetur adipiscing elit. Aliquam vitae porta tellus. Proin ultrices dignissim lacus.
      <div class="pills"><span>More</span><span>API Keys</span></div>
    </div>
  </section>

  <div class="city abs" role="img" aria-label="Photograph of a city skyline with church towers at dusk" style="left:0;top:1343px;width:593px;height:153px"></div>

  <section class="story">
    <p class="body abs" style="left:34px;top:1553px;width:263px">Just how important are customer contacts to a modern business? How important are customers in general for a business? These are trivial questions, because very few companies and business models can function without customers. What's more, key players in the market already recognise that access to complete, timely, high-quality address data has become even more important in the digital age.</p>
    <div class="illus abs" role="img" aria-label="Illustration of a person beside a large tablet displaying data charts" style="left:340px;top:1524px;width:173px;height:173px"></div>
    <div class="illus abs" role="img" aria-label="Illustration of a person using a computer dashboard with a magnifier" style="left:90px;top:1632px;width:193px;height:178px"></div>
    <svg class="abs" style="left:0;top:1660px" width="593" height="260" viewBox="0 0 593 260"><path d="M340 60 C320 110 290 130 250 140 M170 150 C230 175 300 200 330 215 C345 225 310 245 290 255" fill="none" stroke="#5a6ee8" stroke-width="2" stroke-dasharray="5 4"/></svg>
    <p class="body abs" style="left:340px;top:1718px;width:193px">Today, orders can be placed quickly and easily from anywhere in the country. If companies and solutions aren't on hand for potential clients when they need them, they'll just look elsewhere, to another company or even another country. Using wrong or incomplete addresses creates needless work and expense. Key potential customers remain unreached, too, simply because they may have changed their address. Verified and fully updated addresses, on the other hand, allow tried and tested sales campaigns to be organised with guaranteed and timely reach.</p>
    <div class="illus abs" role="img" aria-label="Illustration of a person with a magnifier in front of rising charts" style="left:327px;top:1868px;width:178px;height:170px"></div>
    <p class="body abs" style="left:34px;top:1920px;width:252px">Key information gets to target groups fast, generating results that everyone's pleased with. Set against this backdrop, accurate addresses and records are a key commodity in today's digital economy. With complete address verification or professional address checking, we're able to review these key data assets, identify errors and inaccurate data, compare data with current addresses, carry out targeted address correction and in this way enhance and ready this crucial commodity of modern marketing. So whether you're managing customer contacts, planning a direct marketing campaign or cleaning up old address data, we have the right system for you. Address correction and verification with our tools is the smart and effective way to enhance your data.</p>
    <p class="cta-line abs" style="left:0;width:593px;top:2089px">Get in touch with us. We'll be happy to provide you with further information as well as advice that is personal, secure and discreet.</p>
    <div class="btn-n abs" style="left:243px;top:2117px;width:107px;height:30px">CONTACT US NOW!</div>
  </section>

  <section class="band abs" style="left:0;top:2194px;width:593px;height:282px">
    <h3 class="h3 abs" style="left:33px;top:43px">Specialists in <b>address verification</b></h3>
    <div class="abs" style="left:33px;top:66px;width:285px">
      <p class="body">Handling large volumes of personal data securely, efficiently and in compliance with prevailing legal standards requires smart, considered, proven strategies. Verifying and validating addresses ensures that every entry is reviewed and that the information can be used efficiently for marketing and communications strategies. Every single data point (address, house number, postcode, street) can be individually checked and corrected or changed. Database entries identified as incorrect are rectified and converted into valuable customer data.</p>
      <p class="body">Get in touch with us. We'd love to provide you with more information and show you the value of <b style="color:var(--ink)">market-leading, high-quality digital address verification.</b></p>
    </div>
    <div class="btn-n abs" style="left:33px;top:207px;width:107px;height:30px">CONTACT US NOW!</div>
    <div class="illus-sq abs" role="img" aria-label="Illustration of hands holding a tablet with a line chart and glasses above" style="left:365px;top:37px;width:193px;height:230px;border-radius:50%;opacity:.8"></div>
  </section>

  <footer class="foot abs" style="left:0;top:2476px;width:593px;height:219px">
    <div class="brand dark abs" style="left:33px;top:88px;font-size:11px"><i></i>VERIFONA</div>
    <div class="soc abs" style="left:33px;top:160px"><i></i><i></i><i></i><i></i></div>
    <div class="abs" style="left:204px;top:60px"><h6>PRODUCTS</h6><ul><li>Single Address</li><li>Bulk Validation</li><li>APIs</li></ul></div>
    <div class="abs" style="left:305px;top:60px"><h6>PRICING</h6><ul><li>Germany</li><li>International</li><li>Enterprise</li><li>Private Label/OEM</li><li>Startup</li><li>Competitor Credit</li></ul></div>
    <div class="abs" style="left:416px;top:60px"><h6>RESOURCES</h6><ul><li>Documentation</li><li>Cloud API</li><li>Local API</li><li>SDK</li><li>Articles</li><li>Legal</li><li>System Status</li></ul></div>
    <div class="abs" style="left:527px;top:60px"><h6>COMPANY</h6><ul><li>About Us</li><li>Contact</li><li>Sitemap</li><li>Newsroom</li><li>Blog</li><li>Careers</li><li>Community</li></ul></div>
    <p class="copy abs" style="left:0;width:593px;top:194px">© 2021 verifona.de</p>
  </footer>
</section>

<section class="mob">
  <header class="hero abs" style="left:0;top:0;width:185px;height:250px">
    <div class="brand abs" style="left:20px;top:26px;font-size:8px"><i></i>VERIFONA</div>
    <svg class="abs" style="left:160px;top:26px" width="12" height="8" viewBox="0 0 12 8"><path d="M0 1H12M0 4H12M0 7H12" stroke="#fff"/></svg>
    <p class="abs" style="left:22px;top:90px;width:145px;font-size:6.5px;color:#fff;text-align:center;line-height:10px"><b>ADDRESS VALIDATION:</b> verification &amp; updating | Data quality</p>
    <div class="btn-w abs" style="left:40px;top:148px;width:105px;height:27px">FIND OUT HOW</div>
    <div class="btn-o abs" style="left:40px;top:191px;width:105px;height:27px">FREE TRIAL</div>
  </header>
  <svg class="abs" style="left:88px;top:300px" width="9" height="12" viewBox="0 0 9 12"><path d="M4.5 0a4.5 4.5 0 0 1 4.5 4.5C9 8 4.5 12 4.5 12S0 8 0 4.5A4.5 4.5 0 0 1 4.5 0z" fill="#0e4b8f"/><circle cx="4.5" cy="4.5" r="1.7" fill="#fff"/></svg>
  <p class="kicker abs" style="left:0;width:185px;top:318px;font-size:4.5px">Your most important contact: tomorrow's customer</p>
  <h2 class="abs" style="left:10px;width:165px;top:328px;font-size:7px;font-weight:700;text-align:center;line-height:10px">Complete solutions for professional address validation</h2>
  <article class="feat on abs" style="left:19px;top:378px;width:145px;height:148px">
    <svg class="ico" viewBox="0 0 20 20"><circle cx="8" cy="8" r="6" fill="none" stroke="#fff"/><path d="M12.5 12.5L19 19" stroke="#fff"/></svg>
    <h4><b>Accurate</b> Global Data</h4>
    Lorem ipsum dolor sit amet, consectetur adipiscing elit. Sed a dignissim neque. Pellentesque pellentesque, sapien at finibus iaculis, eros dolor gravida enim, sit amet interdum turpis eros nec felis.
  </article>
  <article class="feat abs" style="left:19px;top:555px;width:145px;height:148px">
    <svg class="ico" viewBox="0 0 20 20"><path d="M2 18L18 2M6 18L18 6M2 14L14 2" stroke="#5a6ee8" fill="none"/></svg>
    <h4><b>Improved</b> Data Quality</h4>
    Lorem ipsum dolor sit amet, consectetur adipiscing elit. Sed a dignissim neque. Pellentesque pellentesque, sapien at finibus iaculis, eros dolor gravida enim, sit amet interdum turpis eros nec felis.
  </article>
  <article class="feat abs" style="left:19px;top:733px;width:145px;height:148px">
    <svg class="ico" viewBox="0 0 20 20"><path d="M10 1L17 19L10 14L3 19Z" stroke="#5a6ee8" fill="none"/></svg>
    <h4><b>Increased</b> Conversions</h4>
    Lorem ipsum dolor sit amet, consectetur adipiscing elit. Sed a dignissim neque. Pellentesque pellentesque, sapien at finibus iaculis, eros dolor gravida enim, sit amet interdum turpis eros nec felis.
  </article>

  <section class="band abs" style="left:0;top:918px;width:185px;height:356px">
    <h3 class="abs" style="left:19px;top:40px;width:150px;font-size:6.5px;line-height:9px"><b>More customer contacts, automatically:</b> address validation works</h3>
    <p class="body abs" style="left:19px;top:72px;width:148px">High data quality is the key competitive advantage in today's digital market. It allows companies to target their resources, communicate efficiently and rest assured that customers are actually being reached. Selling just gets better. Results can be consistently driven higher. We provide solutions for the address verification you need, supporting you with tried and tested processes. Get in touch. We'd love to talk.</p>
    <div class="illus-sq abs" role="img" aria-label="Isometric illustration of a smartphone showing a city map" style="left:37px;top:225px;width:111px;height:111px;border-radius:50%;opacity:.85"></div>
  </section>

  <h3 class="abs" style="left:19px;top:1304px;width:150px;font-size:6.5px;line-height:9px"><b>Address validation as enabler:</b> better contacts just when you need them!</h3>
  <div class="abs" style="left:19px;top:1346px;width:148px">
    <p class="body">The benefits of professional address verification are strikingly simple: information on products, services and solutions gets through to the correct recipients, ensuring improved orders and sales. Accurate data means effective direct marketing efforts.</p>
    <p class="body">And it's not just marketing managers this matters to. Senior leaders, too, take a keen interest in maximising return on investment. The bottom line is that professional address verification means an identical investment simply achieves more.</p>
  </div>
  <h3 class="abs" style="left:19px;top:1562px;width:150px;font-size:6.5px;line-height:9px"><b>Address verification:</b> key information</h3>
  <ul class="list abs" style="left:19px;top:1580px;width:148px">
    <li>Automatic address verification &amp; integration of missing data</li>
    <li>Verification of e-mail or postal addresses</li>
    <li>Address correction based on updated reference data</li>
    <li>Powerful software for modern data management</li>
    <li>Proven functionality with a range of benefits</li>
    <li>Personal advice: verified addresses in a snap</li>
  </ul>

  <h3 class="abs" style="left:19px;top:1755px;font-size:9px;font-weight:400;line-height:10px;color:var(--navy)">OUR<br><b>SOLUTIONS</b></h3>
  <p class="body abs" style="left:19px;top:1783px;width:140px">Discover our outstanding services and get started right away</p>
  <div class="m-list abs" style="left:19px;top:1837px;width:144px;display:grid;gap:15px">
    <div>⌖ Address Service<span>›</span></div>
    <div>⌂ Social Media/eCommerce<span>›</span></div>
    <div>◎ GeoLookup<span>›</span></div>
    <div>◫ Ping Cache<span>›</span></div>
    <div>✉ Email Validation<span>›</span></div>
  </div>

  <div class="city abs" role="img" aria-label="Photograph of a city skyline with church towers" style="left:0;top:1985px;width:185px;height:115px"></div>

  <p class="body abs" style="left:19px;top:2134px;width:148px">Just how important are customer contacts to a modern business? Very few companies and business models can function without customers. Key players in the market already recognise that access to complete, timely, high-quality address data has become even more important in the digital age.</p>
  <div class="illus abs" role="img" aria-label="Illustration of a person beside a tablet displaying data" style="left:37px;top:2266px;width:111px;height:119px"></div>
  <p class="body abs" style="left:19px;top:2407px;width:148px">Today, orders can be placed quickly and easily from anywhere in the country. If companies aren't on hand when clients need them, they'll just look elsewhere. Using wrong or incomplete addresses creates needless work and expense. Key potential customers remain unreached, too, simply because they may have changed their address. Verified and fully updated addresses allow tried and tested sales campaigns with guaranteed and timely reach.</p>
  <div class="illus abs" role="img" aria-label="Illustration of a person using a computer dashboard" style="left:37px;top:2578px;width:111px;height:118px"></div>
  <p class="body abs" style="left:19px;top:2718px;width:148px">Key information gets to target groups fast, generating results that everyone's pleased with. Accurate addresses and records are a key commodity in today's digital economy. With complete address verification, we're able to review these key data assets, identify errors and inaccurate data, compare data with current addresses and carry out targeted address correction. So whether you're managing customer contacts, planning a direct marketing campaign or cleaning up old address data, we have the right system for you.</p>
  <div class="illus abs" role="img" aria-label="Illustration of a person with a magnifier in front of charts" style="left:37px;top:2940px;width:111px;height:119px"></div>
  <p class="cta-line abs" style="left:15px;width:155px;top:3085px;line-height:9px;font-size:5px">Get in touch with us. We'll be happy to provide you with further information as well as advice that is personal, secure and discreet.</p>
  <div class="btn-n abs" style="left:40px;top:3141px;width:105px;height:26px">CONTACT US NOW!</div>

  <section class="band abs" style="left:0;top:3207px;width:185px;height:482px">
    <h3 class="abs" style="left:19px;top:30px;font-size:7px;font-weight:400;white-space:nowrap">Specialists in <b>address verification</b></h3>
    <div class="abs" style="left:19px;top:50px;width:148px">
      <p class="body">Handling large volumes of personal data securely, efficiently and in compliance with prevailing legal standards requires smart, proven strategies. Verifying and validating addresses ensures that every entry is reviewed and can be used efficiently for marketing. Every single data point can be individually checked and corrected. Incorrect entries are rectified and converted into valuable customer data.</p>
      <p class="body">Get in touch with us. We'd love to show you the value of <b style="color:var(--ink)">market-leading, high-quality digital address verification.</b></p>
    </div>
    <div class="btn-n abs" style="left:19px;top:282px;width:105px;height:30px">CONTACT US NOW!</div>
    <div class="illus-sq abs" role="img" aria-label="Illustration of hands holding a tablet with a line chart" style="left:37px;top:356px;width:111px;height:104px;border-radius:50%;opacity:.8"></div>
  </section>

  <footer class="abs" style="left:0;top:3689px;width:185px;height:127px">
    <div class="brand dark abs" style="left:62px;top:40px;font-size:8px"><i></i>VERIFONA</div>
    <div class="soc abs" style="left:68px;top:84px"><i></i><i></i><i></i><i></i></div>
    <p class="copy abs" style="left:0;width:185px;top:104px">© 2021 verifona.de</p>
  </footer>
</section>

</body>
</html>
```